zipPineLeaf

I have a weebly web site need design and formatted using the color and look and feel similar to another site. Our web site is currently behind password. http://www.zippineleaf.com pwd Lantern7Boat!

I'm looking to layout like https://www.quellbirchhub.com/blog

We want a yellow, light yellow, gray and black as the main colors. Attached image show color of yellow and light yellow. I don't have a specific color for gray and black. If you think there should be addition colors in the color pallet we greatly appreciate your expertise.

We need the logo designed. Right now its just text.

I don't like that our site list the full blog one after another, I like the tiled look, image, tile and small amount of text. Click and go into a blog. Often at the end of a blog you can jump back to main page, and/or see three additional blog tiles. We like how orange carries through on buttons and text, Accent colors are consistent.

I need CSS that can be inserted into each form. If you look at the source of the form, you can see how I tried to format given the form elements. I cannot change the form, but I can easily insert CSS for the form.

I need a template that can be used in Weebly site either you edit on our site or give us a template that can be used.

Industry/Entity Type

Life Coaching

Coding

Coded - Design and coding required

Number of Pages Required

5+ page

Font styles to use
Sans Serif

Requirements
Must have
• What to build a clean color pallet using the Yellow, light yellow I uploaded image. Also a gray and black.

```html
<!DOCTYPE html>
<html lang="en">
<head>
<meta charset="utf-8">
<title>zipPineLeaf – Health Blog</title>
<link href="https://fonts.googleapis.com/css2?family=Jost:wght@400;500;600&family=Montserrat:wght@400;500;600;700&family=Roboto+Condensed:wght@700&display=swap" rel="stylesheet">
<style>
:root{
  --accent:#f5413f;
  --ink:#222222;
  --dark:#262626;
  --text:#444444;
  --muted:#777777;
  --line:#dddddd;
  --white:#ffffff;
  --link-blue:#1d5fb0;
}
*{box-sizing:border-box;margin:0;padding:0}
html,body{width:1200px;height:3282px;overflow:hidden;background:var(--white)}
body{position:relative;font-family:"Jost",sans-serif;color:var(--ink)}
.abs{position:absolute}

/* header */
.topbar{left:0;top:0;width:1200px;height:73px;border-bottom:1px solid var(--line)}
.brand{left:71px;top:16px;font:600 33px/40px "Montserrat",sans-serif;color:var(--ink);letter-spacing:-.5px}
.call{left:718px;top:26px;font:400 17px/20px "Jost",sans-serif;color:#444;display:flex;gap:8px;align-items:center}
.call b{font-weight:600;color:var(--ink)}
.btn-sub{left:954px;top:16px;width:166px;height:40px;border-radius:20px;background:var(--accent);color:#fff;font:400 17px/40px "Jost",sans-serif;text-align:center}
.nav{left:0;top:73px;width:1200px;height:56px;display:flex;justify-content:center;gap:46px;font:400 18px/56px "Jost",sans-serif;color:var(--ink);box-shadow:0 2px 4px rgba(0,0,0,.06)}
.nav span{position:relative;padding:0 10px}
.nav .active{color:var(--accent)}
.nav .active:after{content:"";position:absolute;left:0;right:0;bottom:0;height:3px;background:var(--accent)}

/* hero */
.hero{left:0;top:129px;width:1200px;height:564px;background:linear-gradient(180deg,#c9d3e2 0%,#aab8cf 35%,#6f86a6 60%,#3f6288 78%,#557a4a 100%)}
.hero-title{left:120px;top:268px;font:500 60px/70px "Jost",sans-serif;color:#1f2a36}
.hero-sub{left:120px;top:381px;font:400 24px/30px "Jost",sans-serif;color:#1f2a36}
.hero-form{left:116px;top:445px;width:427px;height:49px;border-radius:25px;background:#fff;overflow:hidden}
.hero-form span{position:absolute;left:28px;top:14px;font:400 17px/20px "Jost",sans-serif;color:#666}
.hero-form .go{position:absolute;right:0;top:0;width:68px;height:49px;background:var(--accent)}
.dot{width:14px;height:14px;border-radius:50%;background:#888;left:1080px}
.dot.on{background:#1aa6d8}
.mouse{left:590px;top:601px;width:20px;height:32px;border:2px solid #fff;border-radius:10px}
.mouse:after{content:"";position:absolute;left:7px;top:6px;width:2px;height:7px;background:#fff;border-radius:1px}

/* categories */
.cats{left:0;top:693px;width:1200px;height:178px;background:var(--dark)}
.cat{top:0;height:178px;text-align:center;color:#fff;font:700 20px/24px "Roboto Condensed",sans-serif}
.cat svg{display:block;margin:34px auto 14px}
.cat.on{background:var(--accent)}
.cat.on:after{content:"";position:absolute;left:50%;bottom:-10px;margin-left:-10px;border:10px solid transparent;border-top-color:var(--accent);border-bottom:0}
.divider{top:30px;width:1px;height:112px;background:#666}

/* blog */
.sec-title{left:135px;top:938px;font:600 44px/52px "Montserrat",sans-serif;color:var(--ink)}
.search{left:808px;top:948px;width:260px;height:37px;border-radius:5px;background:#e2e2e2;font:400 14px/37px "Montserrat",sans-serif;color:#555;padding-left:20px}
.search svg{position:absolute;right:16px;top:15px}
.rule{left:132px;top:1013px;width:882px;height:1px;background:var(--line)}
.card{width:292px;height:388px;background:#fff;box-shadow:0 2px 8px rgba(0,0,0,.18)}
.card .ph{position:absolute;left:2px;top:2px;width:288px;height:171px}
.meta{position:absolute;left:26px;top:202px;right:26px;display:flex;justify-content:space-between;font:400 13px/16px "Montserrat",sans-serif;color:#666}
.meta span{display:flex;gap:7px;align-items:center}
.card h3{position:absolute;left:26px;top:238px;font:600 15px/18px "Montserrat",sans-serif;color:var(--ink);letter-spacing:.3px}
.card p{position:absolute;left:26px;top:266px;width:245px;font:400 14px/19px "Montserrat",sans-serif;color:#444}
.card .more{position:absolute;left:26px;top:339px;font:600 13px/16px "Montserrat",sans-serif;color:var(--accent);display:flex;gap:6px;align-items:center}

/* team */
.member{width:177px;height:344px;top:1937px;border-radius:90px;background:#fff;box-shadow:0 3px 10px rgba(0,0,0,.13);text-align:center}
.member .av{position:absolute;left:13px;top:14px;width:151px;height:151px;border-radius:50%}
.member h4{position:absolute;left:0;right:0;top:186px;font:500 17px/22px "Montserrat",sans-serif;color:var(--ink)}
.member small{position:absolute;left:20px;right:20px;top:213px;font:400 13px/16px "Montserrat",sans-serif;color:#555}
.member .social{position:absolute;left:74px;top:267px;width:31px;height:31px;border-radius:50%;background:var(--link-blue)}
.arrow{top:2092px;width:31px;height:31px;border-radius:50%}

/* contact form */
.touch{left:0;top:2365px;width:1200px;text-align:center;font:400 46px/60px "Jost",sans-serif;color:var(--ink)}
.touch b{font-weight:600}
.field{height:47px;border:1.5px solid #999;font:400 18px/44px "Jost",sans-serif;color:#444;padding-left:19px}
.field.msg{height:118px}
.send{left:516px;top:2683px;width:168px;height:47px;border:2px solid #1aa6d8;border-radius:24px;font:400 21px/43px "Jost",sans-serif;text-align:center;color:var(--ink)}

/* footer */
.footer{left:0;top:2873px;width:1200px;height:409px;background:var(--dark)}
.cbox{top:2822px;width:230px;height:122px;background:var(--accent);color:#fff;text-align:center;border-radius:3px}
.cbox h5{font:600 23px/28px "Jost",sans-serif;margin-top:49px}
.cbox.mid h5{margin-top:29px}
.cbox p{font:400 14px/18px "Jost",sans-serif;margin-top:10px}
.cbox.mid p{font-size:17px;line-height:22px;margin-top:8px}
.cicon{top:-14px;left:-4px}
.fcol{color:#fff;font:400 18px/26px "Jost",sans-serif}
.fcol h6{font:400 18px/26px "Jost",sans-serif;margin-bottom:6px}
.fcol a{display:block;color:#fff;text-decoration:underline;font-size:13px;line-height:31px}
.map{left:731px;top:2996px;width:282px;height:109px;background:linear-gradient(135deg,#dfe6ee,#c9d9e6 50%,#e7ecd9);border-bottom:3px solid #f2b233}
.soc{top:3152px;width:31px;height:31px;border-radius:50%;border:1.5px solid #bbb}
.fline{left:27px;top:3210px;width:1173px;height:1px;background:#555}
.fbrand{left:194px;top:3230px;font:600 28px/34px "Montserrat",sans-serif;color:#fff}
.copy{right:182px;top:3238px;font:400 14px/18px "Montserrat",sans-serif;color:#ccc}
</style>
</head>
<body>

<header class="abs topbar"></header>
<div class="abs brand">zipPineLeaf</div>
<div class="abs call">
  <svg width="20" height="20" viewBox="0 0 24 24" fill="none" stroke="#444" stroke-width="1.6"><path d="M5 3h4l2 5-3 2a12 12 0 0 0 6 6l2-3 5 2v4a2 2 0 0 1-2 2A18 18 0 0 1 3 5a2 2 0 0 1 2-2z"/></svg>
  <span>Call us : <b>555-014729</b></span>
</div>
<div class="abs btn-sub">Subscribe Now</div>
<nav class="abs nav">
  <span class="active">Blog</span><span>Who We Are</span><span>Our Model</span><span>Who Uses</span><span>zipPineLeaf</span><span>Pricing</span><span>Contact Us</span>
</nav>

<section class="abs hero" role="img" aria-label="Photo of a person on a rope swing above a misty mountain fjord"></section>
<h1 class="abs hero-title">Finding Joy In Chaos</h1>
<p class="abs hero-sub">Let us help you find a path</p>
<div class="abs hero-form"><span>Subscribe to the zippineleaf</span>
  <div class="go"><svg width="68" height="49" viewBox="0 0 68 49" fill="none" stroke="#fff" stroke-width="2"><path d="M20 24.5h28M40 16l9 8.5-9 8.5"/></svg></div>
</div>
<div class="abs dot" style="top:299px"></div>
<div class="abs dot on" style="top:323px"></div>
<div class="abs dot" style="top:347px"></div>
<div class="abs mouse"></div>

<section class="abs cats">
  <div class="abs cat" style="left:100px;width:170px">
    <svg width="62" height="62" viewBox="0 0 62 62" fill="none" stroke="#fff" stroke-width="2"><circle cx="31" cy="31" r="18"/><circle cx="31" cy="26" r="6"/><path d="M21 42c2-7 18-7 20 0"/><circle cx="10" cy="12" r="5"/><circle cx="52" cy="12" r="5"/><circle cx="10" cy="50" r="5"/><circle cx="52" cy="50" r="5"/></svg>COMMUNITY</div>
  <div class="abs cat on" style="left:294px;width:196px">
    <svg width="62" height="62" viewBox="0 0 62 62" fill="none" stroke="#fff" stroke-width="2"><path d="M31 34C18 24 20 12 27 12c2 0 4 2 4 4 0-2 2-4 4-4 7 0 9 12-4 22z"/><path d="M28 20h6M31 17v6"/><path d="M8 26v14l12 12h8v-8l-9-9M54 26v14L42 52h-8v-8l9-9"/></svg>HEALTH</div>
  <div class="abs cat" style="left:516px;width:170px">
    <svg width="62" height="62" viewBox="0 0 62 62" fill="none" stroke="#fff" stroke-width="2"><circle cx="32" cy="24" r="11"/><path d="M35 19h-5a2 2 0 0 0 0 5h4a2 2 0 0 1 0 5h-5M32 16v16M32 4v5M24 6l2 4M40 6l-2 4"/><path d="M8 44h10l8 4h10a3 3 0 0 1 0 6H24M36 50l14-6a3 3 0 0 1 3 5L38 58H8"/></svg>FINANCE</div>
  <div class="abs divider" style="left:703px"></div>
  <div class="abs cat" style="left:730px;width:170px">
    <svg width="62" height="62" viewBox="0 0 62 62" fill="none" stroke="#fff" stroke-width="2"><circle cx="44" cy="10" r="5"/><path d="M20 22l10-6 8 4-6 12 8 8-6 14M30 32L18 44H6M38 20l8 8h8"/></svg>OBSTACLES</div>
  <div class="abs divider" style="left:926px"></div>
  <div class="abs cat" style="left:946px;width:170px">
    <svg width="62" height="62" viewBox="0 0 62 62" fill="none" stroke="#fff" stroke-width="2"><circle cx="20" cy="8" r="4"/><path d="M20 14v14l-6 12M20 28l6 10v10M14 20l12 4M8 56h48V28H46v8H36v8H26v12"/></svg>CAREER</div>
</section>

<h2 class="abs sec-title">Health</h2>
<div class="abs search">Search<svg width="10" height="6" viewBox="0 0 10 6" fill="none" stroke="#555" stroke-width="1.4"><path d="M1 1l4 4 4-4"/></svg></div>
<div class="abs rule"></div>

<!-- blog cards -->
<article class="abs card" style="left:132px;top:1048px">
  <div class="ph" role="img" aria-label="Photo of a smiling older couple embracing" style="background:linear-gradient(135deg,#d9d4cc,#f2efe9 60%,#cfd8d0)"></div>
  <div class="meta"><span><svg width="14" height="14" viewBox="0 0 14 14" fill="none" stroke="#888"><rect x="1" y="2" width="12" height="11"/><path d="M1 5h12M4 0v3M10 0v3"/></svg>JAN 20, 2020</span><span><svg width="15" height="14" viewBox="0 0 15 14" fill="none" stroke="#888"><ellipse cx="7.5" cy="6.5" rx="6.5" ry="5.5"/><path d="M4 6h7M4 8h5"/></svg>8</span></div>
  <h3>IMPROVISATION</h3>
  <p>Lorem Ipsum is simply dummy text of the printing &amp; typesetting industry. Lorem Ipsum</p>
  <div class="more">LEARN MORE <svg width="6" height="10" viewBox="0 0 6 10" fill="none" stroke="#f5413f" stroke-width="1.8"><path d="M1 1l4 4-4 4"/></svg></div>
</article>
<article class="abs card" style="left:455px;top:1048px">
  <div class="ph" role="img" aria-label="Photo of a hand turning a glowing value dial" style="background:radial-gradient(circle at 55% 55%,#2b4d86,#0d1f3f 70%)"></div>
  <div class="meta"><span><svg width="14" height="14" viewBox="0 0 14 14" fill="none" stroke="#888"><rect x="1" y="2" width="12" height="11"/><path d="M1 5h12M4 0v3M10 0v3"/></svg>JAN 20, 2020</span><span><svg width="15" height="14" viewBox="0 0 15 14" fill="none" stroke="#888"><ellipse cx="7.5" cy="6.5" rx="6.5" ry="5.5"/><path d="M4 6h7M4 8h5"/></svg>8</span></div>
  <h3>STRONG VALUES</h3>
  <p>Lorem Ipsum is simply dummy text of the printing &amp; typesetting industry. Lorem Ipsum</p>
  <div class="more">LEARN MORE <svg width="6" height="10" viewBox="0 0 6 10" fill="none" stroke="#f5413f" stroke-width="1.8"><path d="M1 1l4 4-4 4"/></svg></div>
</article>
<article class="abs card" style="left:776px;top:1048px">
  <div class="ph" role="img" aria-label="Photo of a small tree and globe held in an open hand" style="background:radial-gradient(circle at 55% 40%,#f4f8ee,#a9cf6c 70%,#6aa33a)"></div>
  <div class="meta"><span><svg width="14" height="14" viewBox="0 0 14 14" fill="none" stroke="#888"><rect x="1" y="2" width="12" height="11"/><path d="M1 5h12M4 0v3M10 0v3"/></svg>JAN 20, 2020</span><span><svg width="15" height="14" viewBox="0 0 15 14" fill="none" stroke="#888"><ellipse cx="7.5" cy="6.5" rx="6.5" ry="5.5"/><path d="M4 6h7M4 8h5"/></svg>8</span></div>
  <h3>REALISTIC OPTIMISM</h3>
  <p>Lorem Ipsum is simply dummy text of the printing &amp; typesetting industry. Lorem Ipsum</p>
  <div class="more">LEARN MORE <svg width="6" height="10" viewBox="0 0 6 10" fill="none" stroke="#f5413f" stroke-width="1.8"><path d="M1 1l4 4-4 4"/></svg></div>
</article>
<article class="abs card" style="left:132px;top:1466px">
  <div class="ph" role="img" aria-label="Photo of white spring blossoms on a bright green background" style="background:linear-gradient(135deg,#7fd3d9,#b8e38a 50%,#6fbf3c)"></div>
  <div class="meta"><span><svg width="14" height="14" viewBox="0 0 14 14" fill="none" stroke="#888"><rect x="1" y="2" width="12" height="11"/><path d="M1 5h12M4 0v3M10 0v3"/></svg>JAN 20, 2020</span><span><svg width="15" height="14" viewBox="0 0 15 14" fill="none" stroke="#888"><ellipse cx="7.5" cy="6.5" rx="6.5" ry="5.5"/><path d="M4 6h7M4 8h5"/></svg>8</span></div>
  <h3>LET'S TALK NET WORTH</h3>
  <p>Lorem Ipsum is simply dummy text of the printing &amp; typesetting industry. Lorem Ipsum</p>
  <div class="more">LEARN MORE <svg width="6" height="10" viewBox="0 0 6 10" fill="none" stroke="#f5413f" stroke-width="1.8"><path d="M1 1l4 4-4 4"/></svg></div>
</article>
<article class="abs card" style="left:455px;top:1466px">
  <div class="ph" role="img" aria-label="Photo of an alpine lake in a green mountain valley" style="background:linear-gradient(180deg,#c9d8e6,#8fa88a 40%,#7fb43d 75%,#a8cc3e)"></div>
  <div class="meta"><span><svg width="14" height="14" viewBox="0 0 14 14" fill="none" stroke="#888"><rect x="1" y="2" width="12" height="11"/><path d="M1 5h12M4 0v3M10 0v3"/></svg>JAN 20, 2020</span><span><svg width="15" height="14" viewBox="0 0 15 14" fill="none" stroke="#888"><ellipse cx="7.5" cy="6.5" rx="6.5" ry="5.5"/><path d="M4 6h7M4 8h5"/></svg>8</span></div>
  <h3>IMPROVISATION</h3>
  <p>Lorem Ipsum is simply dummy text of the printing &amp; typesetting industry. Lorem Ipsum</p>
  <div class="more">LEARN MORE <svg width="6" height="10" viewBox="0 0 6 10" fill="none" stroke="#f5413f" stroke-width="1.8"><path d="M1 1l4 4-4 4"/></svg></div>
</article>
<article class="abs card" style="left:776px;top:1466px">
  <div class="ph" role="img" aria-label="Photo of snowy mountains reflected in a blue lake" style="background:linear-gradient(180deg,#3d8fd1,#8ab8da 40%,#4b6f8a 65%,#1f4d72)"></div>
  <div class="meta"><span><svg width="14" height="14" viewBox="0 0 14 14" fill="none" stroke="#888"><rect x="1" y="2" width="12" height="11"/><path d="M1 5h12M4 0v3M10 0v3"/></svg>JAN 20, 2020</span><span><svg width="15" height="14" viewBox="0 0 15 14" fill="none" stroke="#888"><ellipse cx="7.5" cy="6.5" rx="6.5" ry="5.5"/><path d="M4 6h7M4 8h5"/></svg>8</span></div>
  <h3>IMPROVISATION</h3>
  <p>Lorem Ipsum is simply dummy text of the printing &amp; typesetting industry. Lorem Ipsum</p>
  <div class="more">LEARN MORE <svg width="6" height="10" viewBox="0 0 6 10" fill="none" stroke="#f5413f" stroke-width="1.8"><path d="M1 1l4 4-4 4"/></svg></div>
</article>

<!-- team -->
<svg class="abs arrow" style="left:130px" viewBox="0 0 31 31" fill="none" stroke="#444" stroke-width="1.5"><circle cx="15.5" cy="15.5" r="14.5"/><path d="M18 9l-6 6.5 6 6.5"/></svg>
<div class="abs member" style="left:187px"><div class="av" role="img" aria-label="Portrait photo of team member" style="background:#d8d8d8"></div><h4>Daniel Okoth</h4><small>Managing Principal</small><div class="social"></div></div>
<div class="abs member" style="left:404px"><div class="av" role="img" aria-label="Portrait photo of team member" style="background:#d8d8d8"></div><h4>Daniel Okoth</h4><small>Managing Principal</small><div class="social"></div></div>
<div class="abs member" style="left:620px"><div class="av" role="img" aria-label="Portrait photo of team member" style="background:#d8d8d8"></div><h4>Daniel Okoth</h4><small>Managing Principal</small><div class="social"></div></div>
<div class="abs member" style="left:838px"><div class="av" role="img" aria-label="Portrait photo of team member" style="background:#cfcfcf"></div><h4>Peter Langat</h4><small>Management Consultant</small><div class="social"></div></div>
<svg class="abs arrow" style="left:1042px" viewBox="0 0 31 31" fill="none" stroke="#fff" stroke-width="2"><circle cx="15.5" cy="15.5" r="15.5" fill="#f5413f" stroke="none"/><path d="M13 9l6 6.5-6 6.5"/></svg>

<!-- contact form -->
<h2 class="abs touch">Get In <b>Touch</b></h2>
<div class="abs field" style="left:273px;top:2455px;width:314px">Your Name</div>
<div class="abs field" style="left:613px;top:2455px;width:313px;padding-left:72px">Subject</div>
<div class="abs field" style="left:273px;top:2528px;width:314px">Email Address</div>
<div class="abs field msg" style="left:613px;top:2528px;width:313px"></div>
<div class="abs field" style="left:273px;top:2599px;width:314px">Phone</div>
<div class="abs send">Email us</div>

<!-- footer -->
<footer class="abs footer"></footer>
<div class="abs cbox" style="left:231px"><svg class="abs cicon" width="40" height="32" viewBox="0 0 40 32"><rect x="1" y="4" width="38" height="26" fill="#f5413f" stroke="#fff" stroke-width="2"/><path d="M2 5l18 14L38 5" fill="none" stroke="#fff" stroke-width="2"/></svg><h5>Write Us</h5><p>hello@zippineleaf.com</p></div>
<div class="abs cbox mid" style="left:485px"><svg class="abs cicon" width="32" height="44" viewBox="0 0 32 44" style="left:4px;top:-16px"><path d="M16 2a13 13 0 0 1 13 13c0 10-13 27-13 27S3 25 3 15A13 13 0 0 1 16 2z" fill="#f5413f" stroke="#fff" stroke-width="2"/><circle cx="16" cy="15" r="5" fill="#fff"/></svg><h5>Visit Us</h5><p>Lorem Ipsum is<br>simply dummy text of</p></div>
<div class="abs cbox" style="left:739px"><svg class="abs cicon" width="42" height="42" viewBox="0 0 42 42" style="left:-2px;top:-16px"><circle cx="21" cy="21" r="20" fill="#f5413f"/><path d="M11 9h6l3 7-4 3a16 16 0 0 0 8 8l3-4 7 3v6a3 3 0 0 1-3 3A24 24 0 0 1 8 12a3 3 0 0 1 3-3z" fill="none" stroke="#fff" stroke-width="2.2"/></svg><h5>Call Us</h5><p>(000) 555 0147</p></div>

<div class="abs fcol" style="left:187px;top:2991px">Home<br>Who We Are<br>Our Model<br>Who Uses<br>zipPineLeaf</div>
<div class="abs fcol" style="left:363px;top:2995px"><h6>Services</h6><a>Pricing</a><a>Health</a><a>Finance</a></div>
<div class="abs fcol" style="left:530px;top:2990px"><h6>Quick Contact</h6><a>FAQ</a><a>Testimonials</a><a>Contact Us</a></div>
<div class="abs map" role="img" aria-label="Street map showing the office location"></div>
<svg class="abs" style="left:864px;top:3035px" width="16" height="22" viewBox="0 0 16 22"><path d="M8 1a7 7 0 0 1 7 7c0 5-7 13-7 13S1 13 1 8a7 7 0 0 1 7-7z" fill="#e23a3a"/><circle cx="8" cy="8" r="2.5" fill="#fff"/></svg>

<div class="abs soc" style="left:526px"></div>
<div class="abs soc" style="left:565px"></div>
<div class="abs soc" style="left:604px"></div>
<div class="abs soc" style="left:644px"></div>
<div class="abs fline"></div>
<div class="abs fbrand">zipPineLeaf</div>
<div class="abs copy">© 2021 zipPineLeaf. All Rights are Reserved.</div>

</body>
</html>
```